Leading the way in online fitness and education requires power house web design

If you need to contact me you can do so via
skype: Drembal

We need a website designed for new company based in Houston Texas called "DrembalFit". We offer web based training and nutrition programs for our members for example we use the same software as these companies: http://marlowquist.com/ http://www.liftrova.com/ i would like my visitors to be captivated by the level of design creativity of the site.

colors to use would be grey, orange and green.
for example i like the green of this site http://www.cartiva.com/
i will upload my logo files so you can get a feel for shades of grey and orange.

there is a 3d effect filter i would like applied to my logo for use in the web design i have uploaded what that effect looks like.

i will need your designs to be complete with all interior pages which will include Home, Fitness, Nutrition, Fit Lounge, Fit Score, Fit School, Contact Us, Sign up.

fit lounge on my site is the same as pacebin on liftrova and locker room on marlowquist just re branded.

fit school is a research corner for members to learn about health and fitness, we are members of major medical journals on health and fitness and will have all our articles be from the newest research findings.

competitor sites
these sites use same software:
http://marlowquist.com/
http://www.liftrova.com/

these sites are other software.
http://home.stridelogix.com/software-for-athletes.aspx
http://www.vaultrix.com/

here are some websites that i like:
http://www.quorvamedia.com/
http://www.nib-forge.com/
http://velbun.com/
http://www.pralvix.com/
http://www.tormelix.de/fandoloo/
http://brewickstudio.com/

i also like the greens in this site that i am uploading
Updates

I have been reviewing the designs and would like to update everyone at once I do not want a normal fitness website design style, no testimonials, blog post, bodyfat calculator

my website will be a membership based website. i want the website to sell the main points of my fitness app that my members will have access to look at the comments for my selling points, use those points in the site create designs and graphics to visualize those points.

look at these sites and gain inspiration

http://www.dumelo.com.pl/#/projekty/case-studies
http://www.corvane.com/en#/home#ld-qpxn-604217-0039
http://www.nib-forge.com/
http://velbun.com/
http://www.pralvix.com/

i have a few designers asking me what the selling points are, the website needs to be built around these points

main selling points.

overview

programs utilize the best multi-joint exercises combined with high intensity cardio, to give you a full-body workout, efficiently and effectively. This means you’re burning more calories and building more lean muscle per unit of time than traditional weight training and cardio programs.

When you sign up, you''ll receive a work out and diet plan to fit your goals and fitness level. As you progress through your plan, you can use the personal fitness and meal calendar to record your results. When you sign-up we''ll ask you a series of questions and your workouts will be tailored to your exact needs. That means never having to use a generic diet and exercise plan again.

If you''ve ever tried to lose weight and build muscle and didn''t succeed, we feel your pain. Until now, trying to navigate all the fitness fads and latest trends on your own has been difficult. The best option - hiring a certified personal trainer - may be out of your financial reach. That''s where we come in - we''re personal trainers on a mission to help you reach your fitness goals quickly and for less money than in person training. Best of all, we''re here to help you day or night.

Fitness

Personal Fitness Calendar

Tailored to the member’s schedule and flexible to accommodate any changes to a member’s regular fitness schedule. Track your progress and stay on track with your fitness goals.

Custom Fitness Plan

Based on a member’s current physical condition and goals.

• Step by step exercise instructions
• 3-D video demonstrations of over 600 exercises, including functional and body-weight only movements
• Equipment filter can customize plans to your gym’s equipment package
• Record workouts to track exercise history and progression

Nutrition

Nutritional Assessment

Daily recommended caloric intake (Protein, Carbohydrates and Fats), based on personal profile and daily fitness plan.

Custom Meal Plan

Personalized meal plan based on nutritional assessment.

• Choose number of meals per day
• Add dietary restrictions, food preferences or dislikes
• Database of thousands of ingredients allows for hundreds of thousands of meal combinations
• Include favorite foods by entering custom nutritional information

Weight tracking

Calculate goal weight and track weight-loss or weight-gain progress. You will reach your goals in no time.

Fit Lounge

What is the most important part of any workout or fitness program? Staying motivated. And what better form of motivation than positive encouragement from your peers?

Fit Lounge is fitness focused social network for health-minded individuals looking for a simple and convenient place to track their workout goals and monitor their progress. A unique system of motivation, support and accountability makes setting fitness goals and then keeping up with them easy

Track

Start by setting fitness goals that you want to track. They can be anything from running and jogging to how many hours of sleep you are getting and how many glasses of water you are drinking every day. Other members of the drembalfits community might be tracking the same workout goals as you, so you can always join their groups as well.

Share

Once you start tracking your workout goals, you can share your progress with your friends. Reach a new max on your bench press? Let everyone know. Eclipse the 10 mile mark on your daily run? Spread the word! The communication of encouragement back and forth is a great way to ensure that everyone stays on track with their workout goals.

Achieve

Of course, the point of any workout or fitness program is to achieve the goals you’ve set. And with help from drembalfits workout tracking tools and encouragement from the community, you will achieve your workout goals in no time. When you see a friend has achieved his or her fitness goals, you can send them a virtual “fist bump” as a sign of congratulations. The number of “fist bumps” each user accumulates will be displayed on their profile, providing additional motivation and a healthy dose of competition.

Reason: i dont feel the designs i have received are of the quality i am looking for

check this website out, i know its flash, but i also know you can get creative without flash and have nice effects throughout the site.

http://www.lanterfold-hub.com/

I dont want plain jane designs, insert the content i provided into the site and have it explored in a unique way. take as much time on the design as you need as i will keep extending deadline until i find one that is perfect.

as said before don't make the site anything like the competition sites, its only purpose is to sell the memberships using content provided so i need an innovative way to for them to explore that content,

as your designing this site add me on skype so i can detail and help brainstorm ideas my skype id is drembal
you can stray from the color scheme a little or throw it away if you want i just want to see how creative you can get.

Industry/Entity Type

School

Requirements
Nice to have
• if you notice at the bottom of http://marlowquist.com/ she has the orange bar with the three short content parts, i like the idea of having a space like that for similar content.

on http://www.vaultrix.com/ if you look to the left side of the scrolling icons i like the idea of having icons or animated pictures to point of key benefits.

```html
<!DOCTYPE html>
<html lang="en">
<head>
<meta charset="utf-8">
<title>DrembalFit — Personal Training</title>
<link rel="stylesheet" href="https://fonts.googleapis.com/css2?family=Exo+2:ital,wght@0,700;0,800;1,700;1,800;1,900&family=Open+Sans:wght@400;600;700&display=swap">
<style>
:root{
  --orange:#f07a1c;
  --orange-dark:#d8620c;
  --cream:#f4efe8;
  --cream-deep:#e9dfd2;
  --tile:#eadfce;
  --tile-edge:#d9cab5;
  --ink:#2a2a2a;
  --muted:#7b7368;
  --night:#1e1e1e;
  --night-2:#262626;
  --night-line:#3a3a3a;
  --green:#2fa33a;
  --green-dark:#1f7d27;
  --white:#ffffff;
}
*{box-sizing:border-box;margin:0;padding:0}
html,body{width:966px;height:1200px;overflow:hidden;background:var(--cream)}
body{font-family:"Open Sans",Arial,sans-serif;color:var(--ink);position:relative}
.head-font{font-family:"Exo 2",Arial,sans-serif}

/* header */
.site-header{position:absolute;left:0;top:0;width:966px;height:82px;background:var(--cream)}
.brand{position:absolute;left:115px;top:26px;display:flex;align-items:center;gap:8px}
.brand-dot{width:14px;height:14px;border-radius:50%;background:var(--orange)}
.brand-name{font-family:"Exo 2",sans-serif;font-weight:800;font-size:28px;color:#3a3a3a;line-height:1}
.account-links{position:absolute;right:172px;top:15px;display:flex;gap:16px;font-size:10px;font-weight:600;color:#333}
.account-links span{display:flex;align-items:center;gap:4px}
.account-links svg{width:10px;height:10px}
.hotline{position:absolute;right:170px;top:38px;display:flex;align-items:center;gap:8px}
.hotline-label{font-family:"Exo 2",sans-serif;font-style:italic;font-weight:800;font-size:13px;color:#222}
.hotline-number{font-family:"Exo 2",sans-serif;font-weight:800;font-size:23px;color:var(--orange)}

/* nav */
.main-nav{position:absolute;left:0;top:82px;width:966px;height:28px;background:linear-gradient(#f5821f,#e46d12);border-top:1px solid #f79a4a}
.main-nav ul{list-style:none;display:flex;position:absolute;left:115px;top:0;height:28px}
.main-nav li{font-family:"Exo 2",sans-serif;font-style:italic;font-weight:800;font-size:13px;color:var(--white);padding:0 15px;line-height:27px}
.main-nav li.is-active{background:#3a3a3a;border-bottom:3px solid var(--orange-dark)}

/* hero */
.hero{position:absolute;left:0;top:110px;width:966px;height:402px;background:#0b0b0b;overflow:hidden}
.hero-photo{position:absolute;left:115px;top:0;width:680px;height:402px;
  background:radial-gradient(ellipse at 52% 40%,#c9b3a1 0%,#8a7466 22%,#3f5a28 48%,#1c2a12 72%,#0b0b0b 100%)}
.hero-arrow{position:absolute;top:270px;width:54px;height:54px}
.hero-arrow.prev{left:56px}
.hero-arrow.next{left:798px}
.hero-line{position:absolute;font-family:"Exo 2",sans-serif;font-style:italic;font-weight:900;text-transform:uppercase;letter-spacing:-1px;line-height:1}
.hero-line.one{left:145px;top:248px;font-size:50px;color:var(--orange)}
.hero-line.two{left:298px;top:306px;font-size:50px;color:#2b2b2b;text-shadow:0 0 2px #777}

/* selling points */
.selling{position:absolute;left:0;top:512px;width:966px;height:308px;
  background:radial-gradient(ellipse at 50% 20%,#fbf8f3 0%,var(--cream) 50%,var(--cream-deep) 100%)}
.selling-title{position:absolute;left:0;right:0;top:20px;text-align:center;font-family:"Exo 2",sans-serif;font-style:italic;font-weight:900;font-size:26px;color:var(--orange);display:flex;justify-content:center;align-items:center;gap:12px}
.selling-title i{display:block;width:26px;height:3px;background:var(--orange);border-radius:2px}
.points{position:absolute;left:115px;top:66px;width:680px;display:grid;grid-template-columns:333px 333px;column-gap:14px;row-gap:4px}
.point{height:50px;background:linear-gradient(#f3ebdf,var(--tile));border:1px solid var(--tile-edge);border-radius:3px;box-shadow:0 1px 2px rgba(0,0,0,.12);display:flex;align-items:flex-start;padding:10px 10px;gap:8px}
.point.is-featured{background:var(--white)}
.point svg{width:16px;height:16px;flex:none;margin-top:1px}
.point h3{font-family:"Exo 2",sans-serif;font-style:italic;font-weight:800;font-size:12px;color:#222;text-transform:uppercase;line-height:1.1}
.point.is-featured h3{color:var(--orange)}
.point p{font-size:9.5px;color:var(--muted);line-height:1.3}

/* footer */
.site-footer{position:absolute;left:0;top:820px;width:966px;height:230px;background:var(--night-2)}
.footer-col{position:absolute;top:24px}
.footer-col h4{font-family:"Exo 2",sans-serif;font-style:italic;font-weight:800;font-size:12px;color:var(--orange);text-transform:uppercase;margin-bottom:12px;display:flex;align-items:center;gap:6px}
.footer-col h4 i{display:block;width:12px;height:3px;background:var(--orange)}
.footer-col p{font-size:9.5px;line-height:1.55;color:#b8b8b8;text-align:justify}
.footer-col b{color:var(--white);font-weight:600}
.col-school{left:125px;width:210px}
.col-achieve{left:362px;width:198px}
.contact-box{position:absolute;left:587px;top:56px;width:206px;height:58px;background:#0d0d0d;border:1px solid var(--night-line);text-align:center;padding-top:10px}
.contact-box .label{font-family:"Exo 2",sans-serif;font-style:italic;font-weight:800;font-size:11px;color:var(--white)}
.contact-box .number{font-family:"Exo 2",sans-serif;font-weight:800;font-size:18px;color:var(--orange)}
.social{position:absolute;left:587px;top:119px;width:206px;height:52px;display:grid;grid-template-columns:repeat(3,1fr);gap:2px}
.social div{background:#0d0d0d;border:1px solid var(--night-line);display:flex;flex-direction:column;align-items:center;justify-content:center;gap:5px;font-size:8.5px;font-weight:700;color:var(--white);text-transform:uppercase}
.social span.sq{width:20px;height:20px;border-radius:2px;background:#4d6fa8}
.social div:nth-child(2) span.sq{background:#39a9d8}
.social div:nth-child(3) span.sq{background:#1d77b0}

/* copyright */
.copy-tab{position:absolute;left:370px;top:1030px;width:188px;height:22px;background:#1a1a1a;border-top:1px solid var(--night-line);clip-path:polygon(8% 0,92% 0,100% 100%,0 100%);text-align:center;font-family:"Exo 2",sans-serif;font-style:italic;font-weight:800;font-size:11px;color:var(--orange);line-height:22px}
.copy-band{position:absolute;left:0;top:1052px;width:966px;height:148px;background:var(--night)}
.footer-links{position:absolute;left:0;right:0;top:20px;text-align:center;font-size:9px;color:#777}
.footer-links span{padding:0 6px}
.credit{position:absolute;left:0;right:0;top:37px;text-align:center;font-size:9px;color:#777}
.credit b{color:#bbb;font-weight:600}
.join-btn{position:absolute;left:342px;top:63px;width:250px;height:53px;border-radius:3px;background:linear-gradient(#49c04f,var(--green) 55%,var(--green-dark));border:1px solid #17661e;font-family:"Exo 2",sans-serif;font-weight:800;font-size:22px;color:var(--white);text-align:center;line-height:51px;letter-spacing:.5px}
</style>
</head>
<body>

<header class="site-header">
  <div class="brand"><span class="brand-dot"></span><span class="brand-name">DrembalFit</span></div>
  <div class="account-links">
    <span><svg viewBox="0 0 10 10"><rect x="1.5" y="4.5" width="7" height="5" fill="#333"/><path d="M3 4.5V3a2 2 0 0 1 4 0v1.5" stroke="#333" fill="none"/></svg>Login</span>
    <span><svg viewBox="0 0 10 10"><path d="M1 9l1-3 5-5 2 2-5 5z" fill="#333"/></svg>Register</span>
    <span><svg viewBox="0 0 10 10"><path d="M1.5 6V5a3.5 3.5 0 0 1 7 0v1" stroke="#333" fill="none"/><rect x="1" y="5.5" width="2" height="3" fill="#333"/><rect x="7" y="5.5" width="2" height="3" fill="#333"/></svg>Quick Contact</span>
  </div>
  <div class="hotline">
    <svg width="16" height="12" viewBox="0 0 16 12"><path d="M1 4h3l8-3v10L4 8H1z" fill="#222"/></svg>
    <span class="hotline-label">WE'RE HERE TO HELP.</span>
    <span class="hotline-number">1-000-555-0199</span>
  </div>
</header>

<nav class="main-nav">
  <ul>
    <li class="is-active">Home</li><li>Fitness</li><li>Nutrition</li><li>Fit Lounge</li><li>Fit Score</li><li>Fit School</li><li>Contact Us</li>
  </ul>
</nav>

<section class="hero">
  <div class="hero-photo" role="img" aria-label="Photo of a woman running outdoors in a white tank top against a blurred green park"></div>
  <svg class="hero-arrow prev" viewBox="0 0 54 54"><circle cx="27" cy="27" r="24" fill="rgba(0,0,0,.35)" stroke="#555" stroke-width="3"/><path d="M31 17l-10 10 10 10" stroke="#666" stroke-width="3" fill="none"/></svg>
  <svg class="hero-arrow next" viewBox="0 0 54 54"><circle cx="27" cy="27" r="24" fill="rgba(0,0,0,.35)" stroke="#555" stroke-width="3"/><path d="M23 17l10 10-10 10" stroke="#666" stroke-width="3" fill="none"/></svg>
  <div class="hero-line one">DrembalFit Brings</div>
  <div class="hero-line two">A Perfect Health</div>
</section>

<section class="selling">
  <h2 class="selling-title"><i></i>SELLING POINTS<i></i></h2>
  <div class="points">
    <div class="point">
      <svg viewBox="0 0 16 16"><rect x="1" y="3" width="14" height="12" fill="#444"/><rect x="3" y="6" width="10" height="7" fill="#eee"/><path d="M3 9h10M6 6v7M10 6v7" stroke="#444"/></svg>
      <div><h3>Fitness</h3><p>Personal Fitness Calendar</p></div>
    </div>
    <div class="point">
      <svg viewBox="0 0 16 16"><circle cx="9" cy="2.5" r="1.8" fill="#333"/><path d="M8 5l-2 5 3 1-2 4M8 5l3 3 2-1M6 10l-3 1" stroke="#333" stroke-width="1.6" fill="none"/></svg>
      <div><h3>Weight Tracking</h3><p>Calculate goal weight and track weight-loss or weight-gain progress.</p></div>
    </div>
    <div class="point is-featured">
      <svg viewBox="0 0 16 16"><rect x="1" y="3" width="14" height="12" fill="#f07a1c"/><rect x="3" y="6" width="10" height="7" fill="#fff"/><path d="M3 9h10M6 6v7M10 6v7" stroke="#f07a1c"/></svg>
      <div><h3>Custom Fitness Plan</h3><p>Based on a member's current physical condition and goals.</p></div>
    </div>
    <div class="point">
      <svg viewBox="0 0 16 16"><path d="M6 2h4v4h4v4h-4v4H6v-4H2V6h4z" fill="#333" transform="rotate(20 8 8)"/></svg>
      <div><h3>Custom Meal Plan</h3><p>Personalized meal plan based on nutritional assessment.</p></div>
    </div>
    <div class="point">
      <svg viewBox="0 0 16 16"><path d="M8 14S1 9.5 1 5.5A3.5 3.5 0 0 1 8 4a3.5 3.5 0 0 1 7 1.5C15 9.5 8 14 8 14z" fill="#333"/></svg>
      <div><h3>Fit Lounge</h3><p>What is the most important part of any workout or fitness program?</p></div>
    </div>
    <div class="point">
      <svg viewBox="0 0 16 16"><rect x="3" y="1" width="10" height="3" fill="#333"/><path d="M3.5 5h9l-1 10h-7z" fill="#333"/></svg>
      <div><h3>Nutrition</h3><p>Nutritional Assessment</p></div>
    </div>
    <div class="point">
      <svg viewBox="0 0 16 16"><circle cx="4" cy="12" r="2.5" stroke="#333" stroke-width="1.6" fill="none"/><circle cx="12" cy="4" r="2.5" stroke="#333" stroke-width="1.6" fill="none"/><path d="M6 10l4-4" stroke="#333" stroke-width="1.6"/></svg>
      <div><h3>Track</h3><p>Start by setting fitness goals that you want to track.</p></div>
    </div>
    <div class="point">
      <svg viewBox="0 0 16 16"><circle cx="8" cy="5" r="2.3" fill="#333"/><circle cx="3.5" cy="7" r="1.8" fill="#333"/><circle cx="12.5" cy="7" r="1.8" fill="#333"/><path d="M4 14a4 4 0 0 1 8 0z" fill="#333"/><path d="M0.5 14a3 3 0 0 1 4.5-3M15.5 14a3 3 0 0 0-4.5-3" fill="#333"/></svg>
      <div><h3>Share</h3><p>You can share your progress with your friends.</p></div>
    </div>
  </div>
</section>

<footer class="site-footer">
  <div class="footer-col col-school">
    <h4><i></i>Drembal Fit School</h4>
    <p>Lorem ipsum dolor sit amet, consectetur adipiscing elit. Nullam viverra magna non odio dictum tincidunt. Integer orci justo, dictum a ultrices non, tempus nec purus. Lorem ipsum dolor sit amet, consectetur adipiscing elit. Nullam viverra magna non odio dictum tincidunt. Lorem ipsum dolor sit amet, consectetur adipiscing elit. Integer orci justo, dictum a ultrices non, tempus nec purus... <b>READ MORE</b></p>
  </div>
  <div class="footer-col col-achieve">
    <h4><i></i>Achieve</h4>
    <p>Of course, the point of any workout or fitness program is to achieve the goals you've set. And with help from drembalfits workout tracking tools and encouragement from the community, you will achieve your workout goals in no time. When you see a friend has achieved his or her fitness goals, you can send them a virtual "fist bump" as a sign of congratulations. The number of "fist bumps" each user accumulates... <b>READ MORE</b></p>
  </div>
  <div class="contact-box">
    <div class="label">WE'RE HERE TO HELP.</div>
    <div class="number">1-000-555-0199</div>
  </div>
  <div class="social">
    <div><span class="sq"></span>Friendloop</div>
    <div><span class="sq"></span>Chirpline</div>
    <div><span class="sq"></span>Worknet</div>
  </div>
</footer>

<div class="copy-tab">COPYRIGHTS INFO</div>
<div class="copy-band">
  <div class="footer-links"><span>Home</span>|<span>Fitness</span>|<span>Nutrition</span>|<span>Fit Lounge</span>|<span>Fit Score</span>|<span>Fit School</span>|<span>Contact Us</span>|<span>Sign up</span>|<span>Terms of Service</span>|<span>Privacy</span>|<span>Contact</span></div>
  <div class="credit">Copyrights © 2012. <b>Drembalfit.com</b></div>
  <div class="join-btn">JOIN US NOW</div>
</div>

</body>
</html>
```